Brambleford Ponds Trifold About Us Leaflet

I need a A4 Trifold Leaflet Double sided designed with the following information on it:
Logo
Awards
Pictures - Please find on our website www.bramblefordponds.example.co.uk or www.social.example/bramblefordponds
Contact Information
Welcome Text
Events
Ideal for Text
Fishing Text
Camping Text
Map

This is almost a paper version of our website.

```html
<!DOCTYPE html>
<html lang="en">
<head>
<meta charset="utf-8">
<title>Brambleford Ponds Trifold Leaflet</title>
<link href="https://fonts.googleapis.com/css2?family=Mulish:wght@400;600;700;800&display=swap" rel="stylesheet">
<style>
  :root{
    --bg:#9a9a9a;
    --green:#7cb82f;
    --green-light:#a6d64a;
    --green-dark:#3f6b16;
    --grey-band:#8a8a8a;
    --ink:#2b2b2b;
    --white:#ffffff;
  }
  *{margin:0;padding:0;box-sizing:border-box}
  html,body{width:900px;height:1200px;overflow:hidden;background:var(--bg);font-family:"Mulish",sans-serif;color:var(--ink)}
  .sheet{position:absolute;width:652px;height:460px;background:var(--white);box-shadow:4px 5px 8px rgba(0,0,0,.35);overflow:hidden}
  .sheet--outside{left:124px;top:103px}
  .sheet--inside{left:122px;top:603px}
  .sheet svg.shapes{position:absolute;inset:0}
  .abs{position:absolute}
  .pill{background:var(--white);color:var(--ink);font-weight:700;font-size:9px;padding:1px 8px;border-radius:0 8px 8px 0}
  .pill--dark{background:var(--green-dark);color:var(--white)}
  .pill--green{background:var(--green);color:var(--white);font-size:9.5px;border-radius:0 9px 9px 0;padding:2px 8px}
  .body-text{font-size:6px;line-height:1.35;color:var(--white)}
  .body-text p{margin-bottom:4px}
  .contact h2{font-size:11px;font-weight:800;text-align:center;margin-bottom:9px}
  .contact li{list-style:none;font-size:9px;line-height:1.45;display:flex;align-items:center;gap:5px}
  .band-text{color:var(--white);font-size:8.5px;text-align:center;width:217px}
  .brand{font-weight:700;color:var(--green-dark);font-size:18px;letter-spacing:.3px}
  .brand-sub{font-size:8px;font-weight:700;color:var(--green);letter-spacing:.5px}
  .brand-addr{font-size:5px;color:#666}
  .haven{font-size:9px;line-height:12px;text-align:right;width:130px;color:var(--ink)}
  .haven b{color:var(--green);font-weight:800}
  .ideal dt{color:var(--green);font-weight:800;font-size:8px}
  .ideal dd{font-size:7.5px;margin-bottom:5px}
  .events li{list-style:none;font-size:8.5px;margin-bottom:11px}
  .events b{color:var(--green);font-weight:800}
  .further{font-size:10px;line-height:1.5}
  .bullets li{font-size:6px;line-height:1.35;margin-left:10px;color:var(--white)}
  .tariff-title{color:var(--white);font-weight:800;font-size:10.5px;text-align:center;width:190px}
  table.tariff{border-collapse:collapse;width:190px}
  table.tariff td{border:1px solid var(--white);font-size:6px;text-align:center;color:var(--white);padding:3px 0}
  table.tariff tr:last-child td{font-weight:800}
  .tariff-note{font-size:5.2px;color:var(--white);text-align:center;width:190px}
</style>
</head>
<body>

<!-- Outside sheet -->
<section class="sheet sheet--outside">
  <svg class="shapes" width="652" height="460" viewBox="0 0 652 460">
    <defs>
      <linearGradient id="gGreen" x1="0" y1="0" x2="1" y2="1">
        <stop offset="0" stop-color="#a8d94e"/><stop offset="1" stop-color="#6aa524"/>
      </linearGradient>
      <linearGradient id="gSunrise" x1="0" y1="0" x2="0" y2="1">
        <stop offset="0" stop-color="#c98b6a"/><stop offset=".35" stop-color="#8d7a74"/><stop offset="1" stop-color="#3a3d35"/>
      </linearGradient>
      <linearGradient id="gLake" x1="0" y1="0" x2="0" y2="1">
        <stop offset="0" stop-color="#8fb6e0"/><stop offset=".45" stop-color="#dfe7ef"/><stop offset=".6" stop-color="#4d5a3c"/><stop offset="1" stop-color="#5d6f7a"/>
      </linearGradient>
      <linearGradient id="gAngler" x1="0" y1="0" x2="0" y2="1">
        <stop offset="0" stop-color="#7f9a55"/><stop offset="1" stop-color="#3d4a3a"/>
      </linearGradient>
    </defs>
    <rect x="0" y="0" width="217" height="460" fill="url(#gGreen)"/>
    <path d="M0,0 H434 V110 C380,170 280,185 210,170 C130,150 60,100 0,60 Z" fill="url(#gSunrise)" stroke="#fff" stroke-width="5" role="img" aria-label="Photo of a misty sunrise over frosted fields and a fence"/>
    <path d="M0,305 C70,288 150,292 217,330 V460 H0 Z" fill="url(#gAngler)" stroke="#fff" stroke-width="5" role="img" aria-label="Photo of an angler holding a carp beside a young child at the lakeside"/>
    <path d="M434,90 C520,88 610,100 628,120 C645,200 600,280 540,335 C500,375 470,425 450,457 H434 Z" fill="url(#gLake)" stroke="var(--green)" stroke-width="4" role="img" aria-label="Photo of a calm lake reflecting trees and a bright cloudy sky"/>
    <rect x="217" y="434" width="217" height="26" fill="var(--grey-band)"/>
    <rect x="434" y="434" width="218" height="26" fill="var(--grey-band)"/>
    <rect x="258" y="290" width="135" height="90" fill="#eef3e2" role="img" aria-label="Road map showing the route to the park"/>
  </svg>

  <div class="abs pill" style="left:6px;top:159px">About Us:</div>
  <div class="abs body-text" style="left:8px;top:178px;width:190px">
    <p>The Ashworth family established Brambleford Ponds in 1993 from their traditional family farm, over the years it has become home to nightingales, kingfishers, deer and foxes to name but a few.</p>
    <p>Just a short level walk from the campsite there are about 2 miles of off road walking ideal for spotting some of the wildlife or may be just chatting to the fisher folk about the one that got away.</p>
    <p>There is a abundance of local attractions to visit and plenty to see. Whether it is just 1 night or 14 nights Brambleford Ponds welcomes you all.</p>
  </div>

  <div class="abs contact" style="left:217px;top:198px;width:217px">
    <h2>Contact Us:</h2>
    <ul style="margin-left:66px">
      <li><svg width="7" height="7" viewBox="0 0 10 10"><path d="M2 1l2 2-1 1.5c.6 1.2 1.4 2 2.5 2.5L7 6l2 2-1.5 1.5C5 9 1 5 .5 2Z" fill="var(--green)"/></svg>01632 960811</li>
      <li><svg width="7" height="7" viewBox="0 0 10 10"><path d="M2 1l2 2-1 1.5c.6 1.2 1.4 2 2.5 2.5L7 6l2 2-1.5 1.5C5 9 1 5 .5 2Z" fill="var(--green)"/></svg>07700900542</li>
      <li style="font-size:7.5px"><svg width="7" height="7" viewBox="0 0 10 10"><circle cx="5" cy="5" r="4.5" fill="var(--green)"/></svg>www.bramblefordponds.example.co.uk</li>
      <li style="font-size:7.5px"><svg width="7" height="7" viewBox="0 0 10 10"><rect x="0" y="2" width="10" height="7" fill="var(--green)"/><path d="M0 2l5 4 5-4" stroke="#fff" fill="none"/></svg>info@bramblefordponds.example.co.uk</li>
    </ul>
  </div>
  <div class="abs band-text" style="left:217px;top:441px">Electric car charging point is available</div>

  <div class="abs" style="left:434px;top:18px;width:218px;text-align:center">
    <div class="brand">Brambleford Ponds</div>
    <div class="brand-sub">CARAVAN AND CAMPING PARK</div>
    <div class="brand-addr">Ashcombe • Wellmoor • Somerset • ZZ1 0AB &nbsp; Tel: 01632 960811</div>
  </div>
  <div class="abs haven" style="left:512px;top:326px">A haven<br>of <b>peace,</b><br><b>quiet</b> and<br><b>relaxation.</b> So<br>relax, soak up the<br>silence and live life<br>at a gentler pace...</div>
  <div class="abs band-text" style="left:434px;top:441px;font-weight:700;font-size:7.5px">www.bramblefordponds.example.co.uk</div>
</section>

<!-- Inside sheet -->
<section class="sheet sheet--inside">
  <svg class="shapes" width="652" height="460" viewBox="0 0 652 460">
    <defs>
      <linearGradient id="gGreen2" x1="0" y1="0" x2="1" y2="1">
        <stop offset="0" stop-color="#a8d94e"/><stop offset="1" stop-color="#6aa524"/>
      </linearGradient>
      <linearGradient id="gFish" x1="0" y1="0" x2="0" y2="1">
        <stop offset="0" stop-color="#5f7a3c"/><stop offset="1" stop-color="#8a8f6b"/>
      </linearGradient>
      <linearGradient id="gMarquee" x1="0" y1="0" x2="0" y2="1">
        <stop offset="0" stop-color="#1d2a1a"/><stop offset=".5" stop-color="#c9cdd6"/><stop offset="1" stop-color="#141414"/>
      </linearGradient>
      <linearGradient id="gCamp" x1="0" y1="0" x2="0" y2="1">
        <stop offset="0" stop-color="#a9bfd3"/><stop offset=".55" stop-color="#8a7f5e"/><stop offset=".75" stop-color="#e3e5e5"/><stop offset="1" stop-color="#6f9a3a"/>
      </linearGradient>
    </defs>
    <rect x="0" y="0" width="217" height="460" fill="url(#gGreen2)"/>
    <rect x="434" y="0" width="218" height="460" fill="url(#gGreen2)"/>
    <path d="M0,0 H217 V110 C170,150 80,165 0,150 Z" fill="url(#gFish)" stroke="#fff" stroke-width="5" role="img" aria-label="Photo of an angler holding a large carp among reeds"/>
    <path d="M0,372 C70,358 150,368 217,388 V460 H0 Z" fill="url(#gMarquee)" stroke="#fff" stroke-width="5" role="img" aria-label="Photo of a lit marquee at an evening event"/>
    <path d="M336,462 C380,330 500,240 655,212 V462 Z" fill="url(#gCamp)" stroke="#fff" stroke-width="5" role="img" aria-label="Photo of caravans parked on a grassy field under trees"/>
  </svg>

  <div class="abs pill pill--dark" style="left:9px;top:193px">Fishing</div>
  <div class="abs body-text" style="left:10px;top:210px;width:200px;text-align:justify">
    <p>Brambleford Ponds is one of Somerset's best kept secrets for decades, it is surrounded and hidden by a variety of indigenous trees and wildlife. It is an ideal place for a spot of fishing or just watching the wildlife.<br>Brambleford Ponds are 4 acres, stocked with a selection of course fish including carp, bream, tench and others. Ranging to 25lbs.<br>We like to be different, we don't offer pegs to fish from, you can fish anywhere on the bank. There is an onsite toilet and depending on the weather you can drive right to the bankside to save you carrying your fishing gear.</p>
    <p style="text-align:left">£7 per person per day (2 rods)<br>£5 per half day<br>£5 OAP and children 16 and under (under 12s must be accompanied by an adult)</p>
  </div>

  <div class="abs pill pill--green" style="left:230px;top:21px">Brambleford Ponds is ideal for</div>
  <dl class="abs ideal" style="left:231px;top:40px;width:190px">
    <dt>Walking –</dt><dd>The Willow Trail is 220mtrs from the campsite</dd>
    <dt>Cycling –</dt><dd>Somerset is cris crossed with cycle paths</dd>
    <dt>Bird watching –</dt><dd>Over 70 species on site(Bird Trust survey) and there are lots of Bird Trust sites locally</dd>
  </dl>
  <div class="abs pill pill--green" style="left:230px;top:147px;width:60px">Events</div>
  <ul class="abs events" style="left:232px;top:169px">
    <li>Hay Meadow Fair &nbsp;<b>12<sup>th</sup> June</b></li>
    <li>Meadow Games <b>31<sup>st</sup> July</b></li>
    <li>Music by the Ponds &nbsp;<b>13<sup>th</sup> Aug</b></li>
    <li>Family Fun Day <b>27th Aug</b></li>
  </ul>
  <div class="abs further" style="left:232px;top:279px">Further details<br>for any event <b>01632 960811</b></div>

  <div class="abs pill pill--dark" style="left:440px;top:21px">Caravan and Camping</div>
  <div class="abs body-text" style="left:444px;top:38px;width:200px">
    <p>Brambleford Ponds Caravan and Camping Park is located about 1 mile from the historic village of Ashcombe (meaning Great Island, famous for the flooding in 2014) and about 2 miles for the market town of Wellmoor (for shopping and local amenities)</p>
  </div>
  <ul class="abs bullets" style="left:444px;top:84px">
    <li>No set pitches, just level space</li>
    <li>Lots of walks and level cycling</li>
    <li>Award winning dog friendly site</li>
    <li>Easy road access</li>
    <li>Modern toilets and free showers</li>
    <li>Coarse fishing onsite</li>
    <li>Open from 1<sup>st</sup> April to 31<sup>st</sup> October</li>
  </ul>
  <div class="abs tariff-title" style="left:448px;top:147px">Tariff (per night, 2 people)</div>
  <table class="abs tariff" style="left:448px;top:164px">
    <tr><td>April</td><td>May</td><td>June</td><td>July</td><td>August</td><td>Sept.</td><td>Oct.</td></tr>
    <tr><td>£14</td><td>£18</td><td>£20</td><td>£21</td><td>£21</td><td>£18</td><td>£16</td></tr>
  </table>
  <div class="abs tariff-note" style="left:448px;top:201px">Additional Person £3 per night · Electric Hook Up £2 per night</div>
</section>

</body>
</html>
```